Aggressive Inline Skaten für Jugendliche/Kids in Öhringen
Zielgruppe
Meine Zielgruppe sind Kids/Jugendliche. Und die Extrem Sportart "Aggressive Inline Skating" soll von einem professionellen Trainer beigebracht werden.
Aufgabenstellung
Aggressive Inline Skating muss auf jeden Fall rein und das es ein professionelles Training gibt. Preise werden nicht angegeben, da es eine Facharbeit wird und ich noch kein Controlling hatte. Kontaktdaten könnte man evt. einbeziehen falls es von Vorteil ist.
E-Mail Adresse, die Fotos könnte man auch bearbeiten und miteinfügen, es sollte einseitig werden und ein handlicher Flyer werden, der gut überschaubar ist. Also größer wie (Höhe=20cm;Breite=13cm) sollte er nicht sein und evt. vielleicht in der Größe (Höhe=15cm;Breite=10,5). Natürlich kann der Designer aber frei wählen. Und diese Extremsportart wird von einem professionellen Trainer durchgeführt und ist für Kinder und Jugendliche. Ein genaue Altersdefinierung gibt es nicht. Auch könnte man eine Linkverweisung auf Flimmora machen, da es dort aggressive Inline Videos gibt und es ein direkten Bezug gibt, um die Sportart zu zeigen.

```html
<!DOCTYPE html>
<html lang="de">
<head>
<meta charset="utf-8">
<title>Aggressive Inline Skating – Professionelles Training</title>
<link href="https://fonts.googleapis.com/css2?family=Archivo+Black&display=swap" rel="stylesheet">
<style>
  :root {
    --ink: #1f2226;
    --ink-soft: #2c3036;
    --edge-blue: #1f5fb0;
    --title-blue: #2a6fd6;
    --title-blue-deep: #0f3f96;
    --silver: #f2f2f2;
    --silver-shade: #9aa0a6;
    --sky-top: #7fb2d8;
    --sky-low: #e4eef4;
    --ramp: #8c9298;
    --paint: #4b3fa8;
    --page: #e9e9e9;
  }
  * { margin: 0; padding: 0; box-sizing: border-box; }
  html, body { width: 888px; height: 1200px; overflow: hidden; background: var(--page); }
  .flyer {
    position: relative; width: 888px; height: 1200px; overflow: hidden;
    background: var(--ink);
    font-family: "Archivo Black", "Arial Black", sans-serif;
  }
  .photo {
    position: absolute; left: 0; top: 360px; width: 888px; height: 580px;
    background:
      linear-gradient(180deg, transparent 0 58%, rgba(0,0,0,0) 58%),
      linear-gradient(180deg, var(--sky-top) 0%, var(--sky-low) 42%, #5d6b52 52%, var(--ramp) 62%, var(--paint) 82%, #5a5f66 100%);
  }
  .band { position: absolute; left: 0; width: 888px; }
  .band--top { top: 0; height: 440px; }
  .band--bottom { top: 880px; height: 320px; }
  .edge { position: absolute; top: 0; width: 22px; height: 1200px; }
  .edge--left { left: 0; }
  .edge--right { right: 0; }
  .title {
    position: absolute; left: 0; top: 20px; width: 888px;
    transform: rotate(-5deg) skewX(-10deg); transform-origin: 50% 50%;
    text-align: center; line-height: 1;
  }
  .title__kicker {
    display: block; margin-left: -130px; font-size: 62px; letter-spacing: 2px;
    color: var(--title-blue);
    background: linear-gradient(180deg, #8db8ff 0%, var(--title-blue) 45%, var(--title-blue-deep) 100%);
    -webkit-background-clip: text; background-clip: text; -webkit-text-fill-color: transparent;
  }
  .title__main {
    display: block; margin-top: 4px; margin-left: 40px; font-size: 92px; letter-spacing: 1px;
    background: linear-gradient(180deg, #ffffff 0%, var(--silver) 48%, var(--silver-shade) 52%, #e0e0e0 100%);
    -webkit-background-clip: text; background-clip: text; -webkit-text-fill-color: transparent;
    filter: drop-shadow(3px 3px 0 #0b0c0e);
  }
  .title__sub {
    display: block; margin-top: 6px; margin-left: 60px; font-size: 44px; letter-spacing: 2px;
    background: linear-gradient(180deg, #8db8ff 0%, var(--title-blue) 45%, var(--title-blue-deep) 100%);
    -webkit-background-clip: text; background-clip: text; -webkit-text-fill-color: transparent;
  }
  .audience {
    position: absolute; left: 40px; top: 965px; width: 820px;
    transform: rotate(-4deg) skewX(-10deg);
    font-size: 46px; color: var(--silver); letter-spacing: 2px;
    text-shadow: 3px 3px 0 #0b0c0e;
  }
  .contact {
    position: absolute; right: 44px; top: 1070px; text-align: right;
    color: var(--silver); transform: skewX(-10deg);
  }
  .contact__name { font-size: 40px; letter-spacing: 3px; line-height: 1.1; }
  .contact__line { font-size: 19px; letter-spacing: 1px; line-height: 1.45; }
</style>
</head>
<body>
<main class="flyer">
  <div class="photo" role="img" aria-label="Foto: Skater springt mit Inline Skates über eine mit Graffiti bemalte Rampe im Skatepark, Bäume und Himmel im Hintergrund"></div>

  <svg class="band band--top" viewBox="0 0 888 440" preserveAspectRatio="none" aria-hidden="true">
    <path fill="var(--ink)" d="M0 0H888V398L860 404 830 396 790 410 740 398 700 412 650 400 600 414 560 402 510 418 460 404 420 420 380 408 330 424 290 410 240 430 200 414 150 436 110 420 60 440 20 426 0 434Z"/>
    <path fill="var(--ink-soft)" opacity=".6" d="M0 360L120 380 300 370 520 384 700 372 888 386V398L700 412 520 400 300 418 120 422 0 434Z"/>
  </svg>

  <svg class="band band--bottom" viewBox="0 0 888 320" preserveAspectRatio="none" aria-hidden="true">
    <path fill="var(--ink)" d="M0 70L40 60 90 72 140 56 200 66 260 48 320 58 380 40 440 50 500 30 560 42 620 22 680 34 740 14 800 26 850 8 888 14V320H0Z"/>
  </svg>

  <svg class="edge edge--left" viewBox="0 0 22 1200" preserveAspectRatio="none" aria-hidden="true">
    <path fill="var(--edge-blue)" d="M0 0H18L12 120 20 260 10 420 16 560 8 700 18 860 12 1000 20 1200H0Z"/>
  </svg>
  <svg class="edge edge--right" viewBox="0 0 22 1200" preserveAspectRatio="none" aria-hidden="true">
    <path fill="var(--edge-blue)" d="M22 0H4L10 140 2 300 12 460 6 600 14 760 4 920 10 1080 2 1200H22Z"/>
  </svg>

  <h1 class="title">
    <span class="title__kicker">AGGRESSIVE</span>
    <span class="title__main">INLINE SKATING</span>
    <span class="title__sub">PROFESSIONELLES TRAINING</span>
  </h1>

  <p class="audience">FÜR KINDER &amp; JUGENDLICHE</p>

  <address class="contact" style="font-style:normal">
    <div class="contact__name">JONAS BRENNER</div>
    <div class="contact__line">SKATEMIX2001@POSTWERK.DE</div>
    <div class="contact__line">FLIMMORA.COM/USER/BELURAKSCHER1</div>
  </address>
</main>
</body>
</html>
```